Flyer for Beacon Ledger & Returns, a local tax practice

Flyer for my business to be distributed locally in the Western Suburb of Melbourne (Size: DL, Fold: Flat, Backside: Blank) This will include below information (Font, color and capitalization of the text is for the designer's creativity):
Beacon Ledger & Returns Your Local Tax Accountant
ABN: 71 284 519 036
Address: 9 Mirra Close, Tarwin Heights
dovpelk@blrau.com.au
Call Florin on 0417 865 209 to book your appointment
Services we offer:
Individual & Company Tax Returns
Company & Trust formation
Business Advisory
Bookkeeping
BAS & IAS
Payroll
TPAR
Please include the logo of the business attached which was designed by ArtHarbor few years ago.
Please include the QNE, WRD and Pulva logos somewhere in the bottom, preferable the same size and aligned (attached)

```html
<!DOCTYPE html>
<html lang="en">
<head>
<meta charset="utf-8">
<title>Beacon Ledger &amp; Returns – DL Flyer</title>
<link rel="stylesheet" href="https://fonts.googleapis.com/css2?family=Poppins:wght@400;500;600;700;800&display=swap">
<style>
  :root {
    --orange: #e8702a;
    --orange-deep: #d95f1c;
    --charcoal: #48484a;
    --ink: #3a3a3c;
    --paper: #ffffff;
    --card-line: #ececec;
    --backdrop: #d6d6d6;
  }
  * { box-sizing: border-box; margin: 0; padding: 0; }
  html, body { width: 1200px; height: 800px; overflow: hidden; }
  body {
    background: var(--backdrop);
    font-family: "Poppins", sans-serif;
    color: var(--ink);
  }
  .flyer {
    position: absolute;
    left: 420px; top: 19px;
    width: 360px; height: 762px;
    background: var(--paper);
    box-shadow: 0 6px 18px rgba(0,0,0,.22);
    overflow: hidden;
  }
  .brand {
    position: absolute; top: 0; left: 0; width: 100%; height: 104px;
    display: flex; align-items: center; justify-content: center; gap: 10px;
  }
  .brand__square { width: 28px; height: 28px; background: var(--charcoal); }
  .brand__name {
    font-weight: 600; font-size: 19px; color: var(--orange);
    letter-spacing: .2px;
  }
  .hero-photo {
    position: absolute; top: 104px; left: 0; width: 100%; height: 184px;
    background:
      radial-gradient(ellipse at 22% 30%, #f3dcc0 0%, rgba(243,220,192,0) 45%),
      linear-gradient(120deg, #b98d68 0%, #7d5a43 40%, #c9c4c2 70%, #e3e0df 100%);
  }
  .hero-rule {
    position: absolute; top: 288px; left: 26px; width: 304px; height: 2.5px;
    background: var(--orange);
  }
  .headline { position: absolute; top: 306px; left: 0; width: 100%; text-align: center; }
  .headline__kicker { font-weight: 600; font-size: 14px; color: var(--orange); }
  .headline__title {
    font-weight: 800; font-size: 26px; line-height: 31px; color: var(--ink);
    margin-top: 4px; letter-spacing: .5px;
  }
  .services-panel {
    position: absolute; top: 411px; left: 0; width: 102px; height: 169px;
    background: var(--charcoal);
  }
  .services-panel__label {
    position: absolute; top: 44px; left: 27px;
    color: #fff; font-weight: 500; font-size: 14.5px; line-height: 17px;
  }
  .contact-band {
    position: absolute; top: 580px; left: 0; width: 178px; height: 182px;
    background: linear-gradient(160deg, #f08a45 0%, var(--orange) 45%, var(--orange-deep) 100%);
    color: #fff;
  }
  .contact-band__lead { position: absolute; top: 81px; left: 27px; font-weight: 600; font-size: 10px; }
  .contact-band__phone { position: absolute; top: 97px; left: 27px; font-weight: 600; font-size: 22px; letter-spacing: .3px; }
  .contact-band__note { position: absolute; top: 129px; left: 27px; font-weight: 400; font-size: 9px; }
  .service-grid { position: absolute; top: 411px; left: 27px; width: 303px; height: 221px; }
  .service {
    position: absolute; width: 76px; height: 110px;
    background: var(--paper);
    border: 1px solid var(--card-line);
    box-shadow: 0 1px 3px rgba(0,0,0,.06);
    text-align: center;
  }
  .service__icon { display: block; margin: 20px auto 0; }
  .service__name {
    font-weight: 500; font-size: 8.6px; line-height: 10px; color: var(--ink);
    margin-top: 9px;
  }
  .service--low .service__icon { margin-top: 28px; }
  .service--low .service__name { margin-top: 12px; }
  .details {
    position: absolute; top: 640px; left: 195px; width: 160px;
    font-size: 7.6px; line-height: 10px; font-weight: 500;
  }
  .details__row { display: flex; margin-bottom: 3px; }
  .details__key { width: 42px; color: var(--orange); font-weight: 400; }
  .details__val { color: var(--ink); }
  .accreditations {
    position: absolute; top: 712px; left: 195px;
    display: flex; align-items: center; gap: 5px;
  }
</style>
</head>
<body>
  <main class="flyer">
    <header class="brand">
      <span class="brand__square"></span>
      <span class="brand__name">Beacon Ledger &amp; Returns</span>
    </header>

    <div class="hero-photo" role="img" aria-label="Photo of hands working a calculator while holding receipts on a desk"></div>
    <div class="hero-rule"></div>

    <section class="headline">
      <p class="headline__kicker">Beacon Ledger &amp; Returns</p>
      <h1 class="headline__title">YOUR LOCAL<br>TAX ACCOUNTANT</h1>
    </section>

    <div class="services-panel">
      <p class="services-panel__label">Services<br>we offer:</p>
    </div>

    <div class="contact-band">
      <p class="contact-band__lead">Call Florin on</p>
      <p class="contact-band__phone">0417 865 209</p>
      <p class="contact-band__note">to book your appointment</p>
    </div>

    <section class="service-grid">
      <div class="service" style="left:75px;top:0">
        <svg class="service__icon" width="31" height="31" viewBox="0 0 31 31"><circle cx="15.5" cy="15.5" r="15.5" fill="var(--orange)"/><rect x="10" y="8" width="11" height="15" fill="none" stroke="#fff" stroke-width="1.2"/><path d="M12 12h7M12 15h7M12 18h4" stroke="#fff" stroke-width="1.1"/></svg>
        <p class="service__name">Individua<br>&amp; Company<br>Tax Returns</p>
      </div>
      <div class="service" style="left:151px;top:0">
        <svg class="service__icon" width="31" height="31" viewBox="0 0 31 31"><circle cx="15.5" cy="15.5" r="15.5" fill="var(--orange)"/><path d="M10 9h11v7c0 4-5.5 7-5.5 7S10 20 10 16z" fill="none" stroke="#fff" stroke-width="1.2"/><path d="M13 15l2 2 3.5-4" fill="none" stroke="#fff" stroke-width="1.2"/></svg>
        <p class="service__name">Company<br>&amp; Trust<br>formation</p>
      </div>
      <div class="service" style="left:227px;top:0">
        <svg class="service__icon" width="31" height="31" viewBox="0 0 31 31"><circle cx="15.5" cy="15.5" r="15.5" fill="var(--orange)"/><rect x="9" y="9" width="13" height="10" fill="none" stroke="#fff" stroke-width="1.2"/><path d="M11 17l3-3 2 2 4-4M12 23h7" fill="none" stroke="#fff" stroke-width="1.2"/></svg>
        <p class="service__name">Business<br>Advisory</p>
      </div>
      <div class="service service--low" style="left:0;top:111px">
        <svg class="service__icon" width="31" height="31" viewBox="0 0 31 31"><circle cx="15.5" cy="15.5" r="15.5" fill="var(--orange)"/><rect x="9" y="8" width="9" height="15" fill="none" stroke="#fff" stroke-width="1.2"/><rect x="17" y="14" width="6" height="9" fill="none" stroke="#fff" stroke-width="1.2"/><path d="M11 11h5M11 14h4" stroke="#fff" stroke-width="1.1"/></svg>
        <p class="service__name">Bookkeeping</p>
      </div>
      <div class="service service--low" style="left:75px;top:111px">
        <svg class="service__icon" width="31" height="31" viewBox="0 0 31 31"><circle cx="15.5" cy="15.5" r="15.5" fill="var(--orange)"/><rect x="10" y="8" width="11" height="15" fill="none" stroke="#fff" stroke-width="1.2"/><path d="M12 11h7M12 14h7M12 17h7M12 20h4" stroke="#fff" stroke-width="1.1"/></svg>
        <p class="service__name">BAS &amp; IAS</p>
      </div>
      <div class="service service--low" style="left:151px;top:111px">
        <svg class="service__icon" width="31" height="31" viewBox="0 0 31 31"><circle cx="15.5" cy="15.5" r="15.5" fill="var(--orange)"/><circle cx="15.5" cy="10.5" r="3" fill="none" stroke="#fff" stroke-width="1.2"/><path d="M15.5 14v3M10 17h11M10 17v3M15.5 17v3M21 17v3" fill="none" stroke="#fff" stroke-width="1.2"/><circle cx="10" cy="22" r="1.5" fill="#fff"/><circle cx="15.5" cy="22" r="1.5" fill="#fff"/><circle cx="21" cy="22" r="1.5" fill="#fff"/></svg>
        <p class="service__name">Payroll</p>
      </div>
      <div class="service service--low" style="left:227px;top:111px">
        <svg class="service__icon" width="31" height="31" viewBox="0 0 31 31"><circle cx="15.5" cy="15.5" r="15.5" fill="var(--orange)"/><rect x="10" y="8" width="11" height="15" fill="none" stroke="#fff" stroke-width="1.2"/><path d="M12 12h7M12 15h7M12 18h7" stroke="#fff" stroke-width="1.1"/></svg>
        <p class="service__name">TPAR</p>
      </div>
    </section>

    <section class="details">
      <div class="details__row"><span class="details__key">ABN:</span><span class="details__val">71 284 519 036</span></div>
      <div class="details__row"><span class="details__key">Address:</span><span class="details__val">9 Mirra Close,<br>Tarwin Heights</span></div>
      <div class="details__row"><span class="details__key">Email:</span><span class="details__val">dovpelk@blrau.com.au</span></div>
    </section>

    <footer class="accreditations" aria-label="Accreditation badges">
      <svg width="26" height="26" viewBox="0 0 26 26"><circle cx="13" cy="13" r="12" fill="#fff" stroke="#6a6a6a" stroke-width="1.2"/><circle cx="13" cy="13" r="7" fill="#8cc63f"/></svg>
      <svg width="24" height="24" viewBox="0 0 24 24"><circle cx="12" cy="12" r="12" fill="#1ab4e8"/></svg>
      <svg width="24" height="24" viewBox="0 0 24 24"><circle cx="12" cy="12" r="12" fill="#137fa3"/></svg>
      <svg width="44" height="22" viewBox="0 0 44 22"><circle cx="9" cy="11" r="9" fill="#6b3fa0"/><rect x="21" y="7" width="22" height="8" fill="#2b2b5a"/></svg>
    </footer>
  </main>
</body>
</html>
```